Letter Head Design

I need a letter head design based on my company logo that I attached.
Include phone number: (403)582-4316
Address: 347 14th Avenue NE, Calgary, Alberta, Canada, T3K 4R8

Industry/Entity Type

It Company

```html
<!DOCTYPE html>
<html lang="en">
<head>
<meta charset="utf-8">
<title>NovaRoom Interiors Corp. Letterhead</title>
<link href="https://fonts.googleapis.com/css2?family=Open+Sans:wght@400;600;700&display=swap" rel="stylesheet">
<style>
  :root {
    --brand-blue: #2a43f2;
    --brand-green: #5ee31c;
    --paper: #ffffff;
    --faint-blue: #b9cdf6;
    --faint-green: #d4f5c4;
    --white: #ffffff;
  }
  html, body {
    margin: 0;
    padding: 0;
    overflow: hidden;
    background: var(--paper);
  }
  .letterhead {
    position: relative;
    width: 927px;
    height: 1200px;
    overflow: hidden;
    background: var(--paper);
    font-family: "Open Sans", Arial, sans-serif;
  }
  .bands {
    position: absolute;
    inset: 0;
    width: 927px;
    height: 1200px;
  }
  .band-blue { fill: var(--brand-blue); }
  .band-green { fill: var(--brand-green); }

  .header-brand {
    position: absolute;
    top: 20px;
    left: 692px;
    display: flex;
    align-items: center;
    gap: 10px;
  }
  .header-brand .mark {
    width: 50px;
    height: 50px;
    border: 3px solid var(--white);
    border-radius: 6px;
    box-sizing: border-box;
  }
  .header-brand .name {
    color: var(--white);
    font-size: 27px;
    font-weight: 700;
    letter-spacing: -0.5px;
  }

  .watermark {
    position: absolute;
    top: 427px;
    left: 0;
    width: 927px;
    display: flex;
    flex-direction: column;
    align-items: center;
  }
  .watermark .mark {
    width: 236px;
    height: 236px;
    border: 14px solid var(--faint-green);
    border-radius: 16px;
    box-sizing: border-box;
  }
  .watermark .name {
    margin-top: 20px;
    color: var(--faint-blue);
    font-size: 76px;
    font-weight: 600;
    letter-spacing: -1px;
    line-height: 1;
  }

  .footer-contact {
    position: absolute;
    left: 0;
    top: 1154px;
    width: 927px;
    text-align: center;
    color: var(--white);
    font-size: 12.5px;
    font-weight: 600;
    line-height: 18px;
    margin: 0;
  }
</style>
</head>
<body>
<main class="letterhead">
  <svg class="bands" viewBox="0 0 612 792" preserveAspectRatio="none" aria-hidden="true">
    <polygon class="band-blue" points="0,55 402,55 450,0 612,0 612,62 0,62"/>
    <polygon class="band-green" points="0,49 393,49 437,0 445,0 398,53 0,53"/>
    <rect class="band-green" x="0" y="748" width="612" height="9"/>
    <rect class="band-blue" x="0" y="757" width="612" height="35"/>
  </svg>

  <div class="header-brand">
    <span class="mark"></span>
    <span class="name">NovaRoom</span>
  </div>

  <div class="watermark">
    <span class="mark"></span>
    <span class="name">NovaRoom</span>
  </div>

  <address class="footer-contact">
    Address: 347 14th Avenue NE, Calgary, Alberta, Canada, T3K 4R8<br>
    phone number: (403)582-4316
  </address>
</main>
</body>
</html>
```